Two Versions of a Business Card for a Lawyer

Summary: I need a logo and a business card. The business card is two-sided and comes in two versions. One version is conservative, the other is slightly different with one or more pink embellishments in the logo or somewhere else in the business card.
I'm about to start off as a sole practitioner in criminal and immigration law. I'll largely be working with marginalised communities and in areas of social justice. One of my main focuses will be gendered violence, I'm hoping to specialise my practice towards representing victims of domestic and sexual violence and sex workers. I want a business card which would attract this clientele and make them feel safe to speak with me. I'd also like it to communicate a sense of hope.
However, the business card still has to be very conservative as the legal profession is very stuffy. So I was thinking of having two versions of the same card, one would be very straight forward while the other would have a **pink embellishment** or perhaps several. For example, if the scales of justice were used in the design, maybe the second version would have a pink flower about to bloom on the scale somewhere. Or maybe it's my logo that is different and pink.
While both designs have to be pretty conservative, I still want it to give off a sense that I'm alternative and think outside the box. With lawyers, I think a little bit of deviation goes a long way (less is more).
As far as colour goes (other than the pink embellishment), I was thinking something monochromatic, probably black and white but I am open to considering more colours. I personally love colour, and would love to use more colour, but am hesitant because of the nature of the profession. If you can find a way to use more colour while keeping it conservative and letting the pink pop, I'd be pretty pleased.
In general, I would prefer a clean simplistic design and logo. It should be immediately obvious that I'm a lawyer just by glancing at the card. I'm open to symbols of law, like the scales of justice or lady justice or something else. However, I don't want it to be the same as everyone else's.
Eventually, the design/style should be easy to recreate in the form of a website.
As far as the logo goes, it would probably use a circle as my last name starts with the letter "O". It can be very simple, with just my name and "Barrister & Solicitor". I don't currently have a logo, but the winning designer will be invited to provide a separate file for just the logo for an additional fee (I think it was CA$99). (Please ignore the uploaded logo file, it just wouldn't let me continue without uploading something).
As for the information that should go into the card, I'm still finalizing my address and phone number. So please use a placeholder for now.
Target Market(s)
Women, victims of sexual or domestic violence, refugees, people in need of legal services
Industry/Entity Type
Lawyer
Contact Information for Business Card
Maren Vickery
Barrister & Solicitor
LL.B., B.C.L., B.F.A.
Criminal & Immigration Law
Street address
Toronto, ON
Postal Code
Phone number
Fax number
Email
Logo Text
Maren Vickery, Barrister & Solicitor
Requirements
Must have
- Two versions
- One with pink
- Simplistic
Nice to have
- Maybe more colour
Should not have
- Not too conservative
- Not too predictable

```html
<!DOCTYPE html>
<html lang="en">
<head>
<meta charset="utf-8">
<title>Maren Vickery — Business Cards</title>
<link href="https://fonts.googleapis.com/css2?family=Cinzel:wght@500;600&family=Lato:wght@400;700&display=swap" rel="stylesheet">
<style>
  :root {
    --bg: #e9e6e2;
    --ink: #161215;
    --paper: #ffffff;
    --pink: #e0389a;
    --text-dark: #1b181a;
  }
  html, body {
    margin: 0;
    padding: 0;
    width: 1200px;
    height: 891px;
    overflow: hidden;
    background: var(--bg);
  }
  .canvas {
    width: 1200px;
    height: 891px;
    display: flex;
    align-items: center;
    justify-content: center;
    gap: 80px;
  }
  .card {
    position: relative;
    box-shadow: 0 10px 30px rgba(0,0,0,0.18);
    overflow: hidden;
  }

  /* Back of card: black, landscape */
  .card-back {
    width: 560px;
    height: 320px;
    background: var(--ink);
  }
  .card-back .brand-mark {
    position: absolute;
    left: 44px;
    top: 44px;
    display: flex;
    align-items: center;
    gap: 12px;
    font-family: "Lato", sans-serif;
    font-weight: 400;
    font-size: 22px;
    line-height: 1;
    color: var(--paper);
  }
  .brand-mark .brand-dot {
    width: 28px;
    height: 28px;
    border: 2px solid var(--paper);
    border-radius: 50%;
    box-sizing: border-box;
  }
  .card-back .back-name {
    position: absolute;
    right: 44px;
    bottom: 60px;
    font-family: "Cinzel", serif;
    font-weight: 600;
    font-size: 30px;
    color: var(--paper);
    letter-spacing: 1px;
  }
  .card-back .pink-rule {
    position: absolute;
    right: 0;
    bottom: 46px;
    width: 270px;
    height: 5px;
    background: var(--pink);
  }

  /* Front of card: white, portrait */
  .card-front {
    width: 320px;
    height: 560px;
    background: var(--paper);
  }
  .card-front .front-name {
    position: absolute;
    left: 28px;
    top: 40px;
    font-family: "Cinzel", serif;
    font-weight: 600;
    font-size: 32px;
    color: var(--text-dark);
    letter-spacing: 0.5px;
  }
  .card-front .title-band {
    position: absolute;
    left: 22px;
    right: 0;
    top: 92px;
    height: 150px;
    background: var(--ink);
    border-top: 5px solid var(--pink);
    box-sizing: border-box;
    padding: 12px 18px;
    font-family: "Lato", sans-serif;
    font-size: 18px;
    line-height: 1.45;
    color: var(--paper);
  }
  .title-band .credentials span { margin-right: 18px; }
  .card-front .contact {
    position: absolute;
    left: 28px;
    right: 20px;
    bottom: 34px;
    font-family: "Lato", sans-serif;
    font-size: 13px;
    line-height: 1.55;
    color: var(--text-dark);
  }
  .contact .row { display: flex; }
  .contact .label {
    font-weight: 700;
    width: 62px;
    flex-shrink: 0;
  }
  .contact .indent { padding-left: 62px; }
</style>
</head>
<body>
  <main class="canvas">
    <section class="card card-back" aria-label="Card back">
      <div class="brand-mark"><span class="brand-dot"></span><span>Maren Vickery</span></div>
      <div class="back-name">Maren Vickery</div>
      <div class="pink-rule"></div>
    </section>

    <section class="card card-front" aria-label="Card front">
      <div class="front-name">Maren Vickery</div>
      <div class="title-band">
        <div>Barrister &amp; Solicitor</div>
        <div class="credentials"><span>LL.B.</span><span>B.C.L.</span><span>B.F.A.</span></div>
        <div>Criminal &amp; Immigration Law</div>
      </div>
      <div class="contact">
        <div class="row"><span class="label">Adresse:</span><span>Lorem ipsum dolor ifuim</span></div>
        <div class="indent">deom dulir Toronto, ON Postal Code</div>
        <div class="row"><span class="label">Email:</span><span>maren.vickery@mailbox.com</span></div>
        <div class="row"><span class="label">Fax:</span><span>00 00 00 00 00</span></div>
        <div class="row"><span class="label">Phone:</span><span>00 00 00 00 00</span></div>
      </div>
    </section>
  </main>
</body>
</html>
```